Business cards - Yoga Instructor
Quiet Fern Yoga
Creative Brief
Use same font as used in my logo
Use fonts that you feel work well with the logo and style of card
Bright & Fun-filled
Miriam Tovbrask
Certified Yoga Instructor
Fernwell, Ohio
mtovbrask@brightpost.example
www.Quietfern.example
The front should include the "Quiett Fern Yoga" logo that we have uploaded. Also - we would like to include "Offering Veyolin based yoga" on the card as well. perhaps just below the title "Certified Yoga Instructor"
we would like to have the "Ohm" symbol on the back of the card and the words "Strength - Stability - Freedom". here is a link for a sample of the symbol. http://www.breathwheelsite.example/ok.htm We are thinking the Ohm symbol can fill the entire back (even going off the edges) and the text on top.

```html
<!DOCTYPE html>
<html lang="en">
<head>
<meta charset="utf-8">
<title>Miriam Tovbrask – Yoga Instructor Business Cards</title>
<link rel="stylesheet" href="https://fonts.googleapis.com/css2?family=Roboto+Condensed:ital,wght@1,400;1,700&family=Source+Sans+3:ital,wght@0,400;0,600;0,700;1,400;1,600&display=swap">
<style>
  :root {
    --board: #9a9a9c;
    --board-light: #b4b4b6;
    --card-white: #ffffff;
    --pink: #ee5fa8;
    --pink-soft: #f6b5d6;
    --pink-back: #f06fb0;
    --pink-deep: #d9479a;
    --plum: #9b3d8f;
    --plum-dark: #7e2a77;
    --text-grey: #6a5a6a;
    --label: #ec67aa;
    --divider: #e0c4d8;
  }
  * { box-sizing: border-box; margin: 0; padding: 0; }
  html, body { width: 1200px; height: 888px; overflow: hidden; }
  body {
    background: radial-gradient(ellipse at 50% 45%, var(--board-light), var(--board) 75%);
    font-family: "Source Sans 3", Arial, sans-serif;
    position: relative;
  }
  .board-title {
    position: absolute; left: 84px; top: 14px;
    font-family: "Roboto Condensed", Arial, sans-serif; font-style: italic;
    color: #fff; line-height: 1.1;
  }
  .board-title .client { font-size: 29px; font-weight: 700; color: #3a3a3a; }
  .board-title .project { font-size: 26px; font-weight: 400; }

  .variant-label {
    position: absolute; width: 20px; height: 20px; border-radius: 50%;
    background: var(--label); color: #fff; font-size: 9px; font-weight: 600;
    display: flex; align-items: center; justify-content: center;
  }

  .card {
    position: absolute; border-radius: 10px;
    overflow: hidden; box-shadow: 3px 5px 10px rgba(0,0,0,0.35);
  }
  .card-front { width: 492px; height: 230px; background: var(--card-white); }
  .band-top, .band-bottom { position: absolute; left: 0; right: 0; }
  .card-front.soft .band-top { top: 0; height: 30px; background: linear-gradient(to bottom, var(--pink-soft), rgba(255,255,255,0)); }
  .card-front.soft .band-bottom { bottom: 0; height: 40px; background: linear-gradient(to top, var(--pink-soft), rgba(255,255,255,0)); }
  .card-front.bold .band-top { top: 0; height: 22px; background: linear-gradient(to bottom, var(--plum), #d886c4); }
  .card-front.bold .band-bottom { bottom: 0; height: 30px; background: linear-gradient(to top, var(--plum), #d886c4); }

  .brand { position: absolute; left: 40px; top: 42px; width: 230px; text-align: center; }
  .brand-mark { width: 16px; height: 16px; border-radius: 50%; background: var(--pink); margin: 0 auto 4px; }
  .brand-name { font-weight: 600; font-size: 28px; color: var(--plum); white-space: nowrap; }

  .instructor { position: absolute; left: 30px; top: 130px; white-space: nowrap; }
  .instructor-name { font-size: 18px; color: var(--plum); }
  .instructor-title { font-size: 11.5px; color: var(--text-grey); margin-top: 1px; }
  .divider { position: absolute; left: 282px; top: 96px; width: 1px; height: 104px; background: var(--divider); }
  .offering { position: absolute; left: 292px; top: 98px; font-size: 11px; font-style: italic; color: var(--plum); white-space: nowrap; }
  .contact-list { position: absolute; left: 292px; top: 122px; list-style: none; }
  .contact-list li { display: flex; align-items: center; height: 18px; font-size: 10.5px; color: var(--text-grey); white-space: nowrap; }
  .contact-list svg { width: 10px; height: 10px; margin-right: 9px; fill: var(--plum); flex: none; }

  .card-front.bold .instructor { left: 296px; top: 74px; }
  .card-front.bold .instructor-name { font-size: 13px; }
  .card-front.bold .instructor-title { font-size: 10px; }
  .card-front.bold .offering { left: 296px; top: 108px; font-size: 10px; }
  .card-front.bold .contact-list { left: 296px; top: 126px; }

  .card-back { width: 480px; height: 290px; background: radial-gradient(ellipse at 50% 60%, #f58cc2, var(--pink-back) 70%, var(--pink-deep)); }
  .sun-om {
    position: absolute; left: 90px; top: 20px; width: 300px; height: 300px; border-radius: 50%;
    background: radial-gradient(circle, #c5428f 0%, #d9559e 30%, rgba(240,130,190,0.55) 55%, rgba(240,111,176,0) 72%);
  }
  .card-back.light .sun-om {
    background: radial-gradient(circle, #f9c4de 0%, #f7acd1 30%, rgba(250,190,220,0.5) 55%, rgba(240,111,176,0) 72%);
  }
  .tagline-arc { position: absolute; left: 0; top: 0; width: 480px; height: 290px; }
  .tagline-arc text { font-family: "Source Sans 3", Arial, sans-serif; font-size: 24px; fill: #fff; }
  .tagline-straight {
    position: absolute; left: 0; right: 0; top: 36px; text-align: center;
    font-size: 24px; font-style: italic; font-weight: 600; color: var(--plum); white-space: nowrap;
  }
  .back-web {
    position: absolute; left: 0; right: 0; bottom: 22px; text-align: center;
    font-size: 12px; font-weight: 700; color: #fff;
  }
  .card-back.light .back-web { color: var(--plum-dark); }
</style>
</head>
<body>
  <header class="board-title">
    <div class="client">Miriam Tovbrask</div>
    <div class="project">Yoga Instructor - Business cards</div>
  </header>

  <!-- Front, soft pink -->
  <div class="variant-label" style="left:96px;top:184px;">1a</div>
  <section class="card card-front soft" style="left:96px;top:214px;">
    <div class="band-top"></div><div class="band-bottom"></div>
    <div class="brand"><div class="brand-mark"></div><div class="brand-name">Quiet Fern Yoga</div></div>
    <div class="instructor">
      <div class="instructor-name">Miriam Tovbrask</div>
      <div class="instructor-title">Certified Yoga Instructor</div>
    </div>
    <div class="divider"></div>
    <div class="offering">Offering Veyolin based yoga</div>
    <ul class="contact-list">
      <li><svg viewBox="0 0 12 12"><rect x="1" y="2" width="10" height="8" rx="1"/></svg>Fernwell, Ohio</li>
      <li><svg viewBox="0 0 12 12"><path d="M2 1h3l1 3-2 1a7 7 0 0 0 3 3l1-2 3 1v3a1 1 0 0 1-1 1A10 10 0 0 1 1 2a1 1 0 0 1 1-1z"/></svg>(555) 555-0148</li>
      <li><svg viewBox="0 0 12 12"><circle cx="6" cy="6" r="6"/></svg>mtovbrask@brightpost.example</li>
      <li><svg viewBox="0 0 12 12"><circle cx="6" cy="6" r="5" fill="none" stroke="#9b3d8f" stroke-width="1.5"/><path d="M1 6h10M6 1v10" stroke="#9b3d8f" stroke-width="1"/></svg>www.Quietfern.example</li>
    </ul>
  </section>

  <!-- Front, plum bands -->
  <div class="variant-label" style="left:614px;top:184px;">1b</div>
  <section class="card card-front bold" style="left:619px;top:214px;width:470px;">
    <div class="band-top"></div><div class="band-bottom"></div>
    <div class="brand"><div class="brand-mark"></div><div class="brand-name">Quiet Fern Yoga</div></div>
    <div class="instructor">
      <div class="instructor-name">Miriam Tovbrask</div>
      <div class="instructor-title">Certified Yoga Instructor</div>
    </div>
    <div class="offering">Offering Veyolin based yoga</div>
    <ul class="contact-list">
      <li><svg viewBox="0 0 12 12"><rect x="1" y="2" width="10" height="8" rx="1"/></svg>Fernwell, Ohio</li>
      <li><svg viewBox="0 0 12 12"><path d="M2 1h3l1 3-2 1a7 7 0 0 0 3 3l1-2 3 1v3a1 1 0 0 1-1 1A10 10 0 0 1 1 2a1 1 0 0 1 1-1z"/></svg>(555) 555-0148</li>
      <li><svg viewBox="0 0 12 12"><circle cx="6" cy="6" r="6"/></svg>mtovbrask@brightpost.example</li>
      <li><svg viewBox="0 0 12 12"><circle cx="6" cy="6" r="5" fill="none" stroke="#9b3d8f" stroke-width="1.5"/><path d="M1 6h10M6 1v10" stroke="#9b3d8f" stroke-width="1"/></svg>www.Quietfern.example</li>
    </ul>
  </section>

  <!-- Back, white arched tagline -->
  <div class="variant-label" style="left:96px;top:492px;">1c</div>
  <section class="card card-back" style="left:94px;top:492px;transform:rotate(-3deg);">
    <div class="sun-om" role="img" aria-label="Radiating sun rays around a large om symbol"></div>
    <svg class="tagline-arc" viewBox="0 0 480 290">
      <defs><path id="arc-1c" d="M40 160 Q240 20 440 160"/></defs>
      <text><textPath href="#arc-1c" startOffset="50%" text-anchor="middle">Strength • Stability • Freedom</textPath></text>
    </svg>
    <div class="back-web">Quietfern.example</div>
  </section>

  <!-- Back, plum straight tagline -->
  <div class="variant-label" style="left:614px;top:492px;">1d</div>
  <section class="card card-back light" style="left:614px;top:498px;transform:rotate(2deg);">
    <div class="sun-om" role="img" aria-label="Pale radiating sun rays around a large om symbol"></div>
    <div class="tagline-straight">Strength • Stability • Freedom</div>
    <div class="back-web">Quietfern.example</div>
  </section>
</body>
</html>
```